Lumigrove Pages with Bold Font

I want the font to be simple yet bold for Lumigrove images. Its all about a simple bold readable font. I need a single lumigrove page with an image and copy/text on or over the image. The words will change in the future. I'm looking for the right font. I like fiery red and yellow colors. The "One Pic" attached is a sample of what I want without the Velnor words.

```html
<!DOCTYPE html>
<html lang="en">
<head>
<meta charset="UTF-8">
<title>Lumigrove Page – Trainer Quote</title>
<link href="https://fonts.googleapis.com/css2?family=Montserrat:wght@400;600;700&display=swap" rel="stylesheet">
<style>
  :root {
    --red-bright: #d0142c;
    --red-mid: #b10d22;
    --red-deep: #6e0612;
    --gold: #f5c400;
    --white: #ffffff;
    --blush: #eadbe0;
    --photo-light: #e9a98a;
    --photo-mid: #c97a5c;
    --photo-dark: #9c4a36;
  }
  html, body {
    margin: 0;
    padding: 0;
    overflow: hidden;
    background: var(--red-deep);
  }
  .page {
    position: relative;
    width: 1200px;
    height: 1200px;
    overflow: hidden;
    font-family: "Montserrat", Arial, sans-serif;
    background:
      radial-gradient(ellipse at 65% 25%, var(--red-bright) 0%, var(--red-mid) 55%, var(--red-deep) 100%);
  }
  .portrait {
    position: absolute;
    left: 0;
    top: 18px;
    width: 530px;
    height: 1182px;
    border-radius: 240px 240px 0 0;
    background: linear-gradient(180deg, var(--photo-light) 0%, var(--photo-mid) 55%, var(--photo-dark) 100%);
  }
  .byline {
    position: absolute;
    right: 66px;
    top: 112px;
    text-align: right;
    color: var(--white);
    font-size: 34px;
    line-height: 48px;
  }
  .byline-name { font-weight: 700; }
  .byline-role { font-weight: 400; }
  .divider {
    position: absolute;
    right: 66px;
    top: 250px;
    width: 53px;
    height: 2px;
    background: var(--white);
  }
  .quote {
    position: absolute;
    right: 66px;
    top: 292px;
    margin: 0;
    text-align: right;
    color: var(--gold);
    font-weight: 700;
    font-size: 59px;
    line-height: 75px;
    letter-spacing: 0.5px;
    text-shadow: 2px 3px 4px rgba(60, 0, 0, 0.45);
  }
  .thanks {
    position: absolute;
    right: 66px;
    top: 890px;
    margin: 0;
    color: var(--blush);
    font-weight: 700;
    font-size: 55px;
    letter-spacing: 0.5px;
  }
</style>
</head>
<body>
  <main class="page">
    <div class="portrait" role="img" aria-label="Photo of the trainer posing against the red backdrop"></div>

    <div class="byline">
      <div class="byline-name">Dana Rae Quill</div>
      <div class="byline-role">Trainer for Men</div>
    </div>
    <div class="divider"></div>

    <p class="quote">“Everybody wanted<br>me to make big<br>drastic changes in<br>my life. I can’t do<br>that.&nbsp; All these little<br>“Tricks of the Trade”<br>I can do that.”</p>

    <p class="thanks">Thank you Dana.</p>
  </main>
</body>
</html>
```